Photography Studio Prep Guide Design Needed

I have a prep guide I send to all parents who book a session - It is outdated and ugly. I want a gorgeous, clean, modern upscale look for the brochure I send.

I already have the text and can provide photos for the final design. I want the cover to be clean and upscale and modern, with a happy feel.

Target Market(s)

My clients for an upscale Newborn Photography Studio

Requirements
Must have
• space for my photos, an upscale clean feel
Nice to have
• I love color, but don't want the brochure to look busy. I love cream, white, pale pink.

```html
<!DOCTYPE html>
<html lang="en">
<head>
<meta charset="utf-8">
<title>Newborn Session Prep Guide</title>
<link href="https://fonts.googleapis.com/css2?family=Oswald:wght@400;500&family=Raleway:wght@200;300;400;600&family=Parisienne&display=swap" rel="stylesheet">
<style>
:root{
  --cover-pink:#dc93a9;
  --rose:#c9718f;
  --rose-soft:#e7b3c3;
  --blush:#f6dde5;
  --cream:#f7f1ea;
  --ink:#555055;
  --ink-strong:#332f33;
  --white:#ffffff;
  --sans:'Raleway', Arial, sans-serif;
  --head:'Oswald', 'Arial Narrow', sans-serif;
  --script:'Parisienne', cursive;
}
*{box-sizing:border-box;margin:0;padding:0}
html,body{width:1200px;height:1200px;overflow:hidden;background:var(--white)}
body{position:relative;font-family:var(--sans);color:var(--ink)}
.page{position:absolute;width:389px;height:486px;overflow:hidden;background:var(--white);border:1px solid #d9d2d4}
.page--cover{left:20px;top:64px;background:var(--cover-pink)}
.page--p2{left:409px;top:64px}
.page--p3{left:798px;top:64px}
.page--p4{left:20px;top:580px}
.page--p5{left:409px;top:580px}
.page--p6{left:798px;top:580px}
.frame{position:absolute;inset:6px;border:2px solid var(--rose-soft);pointer-events:none}
.page--cover .frame{border:1px solid var(--white)}
.photo{position:absolute}

/* cover */
.cover-name{position:absolute;left:0;right:0;top:84px;text-align:center;color:var(--white);font:300 11px/1 var(--sans);letter-spacing:4px}
.cover-title{position:absolute;left:0;right:0;top:190px;text-align:center;color:var(--white);font:200 30px/1 var(--sans);letter-spacing:.5px}
.cover-sub{position:absolute;left:0;right:0;top:224px;text-align:center;color:var(--white);font:34px/1 var(--script)}
.cover-photo{left:6px;right:6px;top:268px;bottom:6px;background:radial-gradient(ellipse at 50% 45%,#f1d6c8 0%,#e9b6ba 45%,var(--cover-pink) 80%)}

/* text pages */
.content{position:absolute;left:14px;right:12px;top:14px}
.mini-name{text-align:center;color:var(--rose);font:400 7px/1 var(--sans);letter-spacing:2px;margin-top:12px}
.script-title{text-align:center;color:var(--rose);font:20px/1.1 var(--script);margin-top:10px}
.intro{text-align:center;font:300 8px/1.35 var(--sans);color:var(--ink-strong);margin-top:4px}
.sec-h{color:var(--rose);font:500 11px/1 var(--head);text-transform:uppercase;margin:13px 0 5px}
p.body{font:300 7.4px/1.42 var(--sans);color:var(--ink-strong)}
p.body b{font-weight:600}
.p2-photo{left:103px;top:326px;width:280px;height:154px;background:linear-gradient(90deg,#fff 0%,#eadfd9 40%,#d9c3b6 70%,#fff 100%)}
.p3-photo{left:6px;right:6px;top:0;height:66px;background:linear-gradient(90deg,#f2c9d3,#ecd9d6 50%,#f2c9d3)}
.page--p3 .content{top:74px}
.page--p3 .sec-h{margin:10px 0 4px}
.trio{position:absolute;left:0;right:0;top:122px;height:126px;display:flex;gap:5px}
.trio div{flex:1}
.trio-a{background:linear-gradient(135deg,#f3ede4,#e0d3c2)}
.trio-b{background:linear-gradient(135deg,#d8ece6,#a9d6c9)}
.trio-c{background:linear-gradient(135deg,#8c5c7f,#b79ac0)}
.p4-lower{position:absolute;left:14px;right:12px;top:258px}
.p5-photo{inset:0;background:radial-gradient(ellipse at 50% 70%,#efe6d8 0%,#f5efe6 55%,#f8f3ec 100%)}

/* checklist page */
.need-list{list-style:none;margin-top:10px}
.need-list li{display:flex;gap:10px;align-items:flex-start;margin-bottom:9px}
.num{flex:none;width:22px;height:22px;border-radius:50%;background:var(--rose);color:var(--white);font:17px/22px var(--script);text-align:center}
.need-list p{font:300 7.2px/1.4 var(--sans);color:var(--ink-strong);padding-top:1px}
.faq-title{text-align:center;color:var(--rose);font:500 18px/1 var(--head);margin:4px 0 6px}
.faq-q{display:block;width:max-content;margin:8px auto 4px;background:var(--rose);color:var(--white);font:400 8.5px/1 var(--head);padding:2px 5px;text-transform:uppercase}
.faq-a{text-align:center;font:300 7.2px/1.4 var(--sans);color:var(--ink-strong)}
.circles{position:absolute;left:20px;right:20px;top:382px;display:flex;justify-content:space-between}
.circles div{width:88px;height:88px;border-radius:50%}
.c1{background:radial-gradient(circle,#f1dde0,#c4a3cf)}
.c2{background:radial-gradient(circle,#f4eee8,#ffffff)}
.c3{background:radial-gradient(circle,#f3d8cf,#e6c2bb)}
</style>
</head>
<body>

<section class="page page--cover">
  <div class="cover-name">CLARA BELLAMY PHOTOGRAPHY</div>
  <h1 class="cover-title">NEWBORN SESSION</h1>
  <div class="cover-sub">Prep Guide</div>
  <div class="photo cover-photo" role="img" aria-label="Client photo: smiling baby wearing a floral crown lying on a pink blanket"></div>
  <div class="frame"></div>
</section>

<section class="page page--p2">
  <div class="frame"></div>
  <div class="content">
    <div class="mini-name">CLARA BELLAMY</div>
    <h2 class="script-title">Parent Instructions &amp; Preparations</h2>
    <p class="intro">Congratulations on expecting a baby!<br>Here are my instructions to ensure a successful newborn photography session.<br>Please follow these instructions as closely as possible.</p>
    <h3 class="sec-h">1. Nursing</h3>
    <p class="body">If you are nursing, please avoid eating anything spicy (hot sauce, hot peppers, curry, etc.) that might upset baby's tummy for 24 hours preceding your scheduled session.<br>Please if you are breastfeeding do NOT drink caffeine or coffee before your session – I know this is hard but baby will be wired if you have caffeine.<br>If you notice baby has a lot of gas after feedings please check with your pediatrician and bring gas drops (TummyCalm or other brand) to your session. The most common reason a baby will not settle for a session is gas pressure/discomfort.</p>
    <h3 class="sec-h">2. Feeding</h3>
    <p class="body">Feed the baby as much as possible in the 24 hours preceding your session – this will help minimize the amount baby needs to feed during the session, and will help baby sleep as long and as soundly as possible. Feed baby 2-3 hours before your session and not again until you arrive. This feeding is planned in your session time and it's not rushed.<br><b>Please bring an extra bottle of formula or breastmilk to the session if possible – sometimes a small amount of milk in a bottle can quickly soothe a baby back to sleep without requiring a full feeding.</b> I will respect your wishes if you choose not to use a bottle, but please understand we may have to pass on some poses if baby will not settle in position, and I cannot use a bottle to soothe them into the pose.</p>
  </div>
  <div class="photo p2-photo" role="img" aria-label="Client photo: mother lifting her baby above her"></div>
</section>

<section class="page page--p3">
  <div class="photo p3-photo" role="img" aria-label="Client photo: sleeping newborn with a flower headband on pink fur"></div>
  <div class="frame"></div>
  <div class="content">
    <h3 class="sec-h">3. Keep Baby Awake</h3>
    <p class="body">Interact with, and <b>keep baby awake for 2 hours preceding your appointment to make sure they are nice and sleepy for their session.</b> A great way to do this is by giving baby a bath – which will get them nice and clean and keep them awake.<br>Also – keeping baby naked, in a diaper only is a good way to keep them awake and alert. This step is extremely important – <b>otherwise it can take a long time to get baby to sleep, and we will have less time for photos.</b></p>
    <h3 class="sec-h">4. Clothes</h3>
    <p class="body">Please dress baby in a simple loose sleeper we can just unsnap when you arrive – we want to keep baby as calm and happy as possible and want to avoid clothes we have to pull over their head. I provide all clothing/hats/props at your session.</p>
    <h3 class="sec-h">5. Pacifier</h3>
    <p class="body">Please bring a pacifier – it can be very helpful during a session if a baby is fussy.<br>Please note I only use the pacifier for a few minutes at a time to soothe into a pose.<br><b>If you choose not to bring a pacifier I will respect your decision, but please understand we may have to pass on several poses if you do not bring one.</b></p>
    <h3 class="sec-h">6. Studio</h3>
    <p class="body">My studio is kept VERY warm to make sure your baby is comfortable through the whole session. It will be around 75-80 degrees so please dress in layers for comfort. I will have cold bottles of water available during your session.<br><b>Please note – if you ask me to turn the heat down, or tell me it is too warm for baby, I cannot guarantee any results for your session.</b> Babies are used to 98.6 degrees in the womb, and a cold studio will wake baby immediately. Babies do not wear much during their sessions and lose heat quickly. If you ask me to turn the heat down, and baby is fussy I will finish the session with only swaddled poses, or with parents. It is not safe to put an awake, alert baby in any props.</p>
    <h3 class="sec-h">7. Your Role</h3>
    <p class="body">Your role at this session is to sit back and relax. I need very little assistance during the session, and want you to take this time to rest, relax and enjoy the session. Feel free to nap, catch up on work, thank you notes, or whatever you like. If baby needs to feed during the session that will be your only task! I will occasionally ask for a spotter for safety on some poses.</p>
  </div>
</section>

<section class="page page--p4">
  <div class="frame"></div>
  <div class="content">
    <h3 class="sec-h">8. Time</h3>
    <p class="body">Your session will last between 2-4 hours- please keep this in mind. I will provide bottled water and light snacks (granola bars/pretzels/etc.) but you may want to bring more food since the session can last up to 4 hours. <b>Please note that I cannot shoot past 4 hours – if baby is fussy I will do my best to get beautiful photos. At 3 hours if baby is still fussy I will let you know that we need to switch to swaddled/wrapped poses to finish the session. Or we can do more family photos as well.</b></p>
  </div>
  <div class="trio">
    <div class="trio-a" role="img" aria-label="Client photo: newborn in a cream wrap in a woven basket"></div>
    <div class="trio-b" role="img" aria-label="Client photo: newborn curled on a mint wrap"></div>
    <div class="trio-c" role="img" aria-label="Client photo: newborn in lavender surrounded by purple flowers"></div>
  </div>
  <div class="p4-lower">
    <h3 class="sec-h">9. Family Photos/Clothing</h3>
    <p class="body">I highly recommend mom and dad wear simple white/cream shirts, or black/navy shirts which will keep the focus on the baby. Mom can choose a tank top or dress as well. That is only a suggestion, and of course you are welcome to wear anything you choose. If dad is comfortable baring his chest it can make for some beautiful images, but that is totally up to the comfort of dad! My photos of newborns with mom/dad are generally from the waist up, so your pants or shoes will not matter.</p>
    <h3 class="sec-h">10. Sibling Photo</h3>
    <p class="body">Photos of your newborn with their sibling(s) are included, and will be done at the very beginning of the session. I recommend having sibling boys wear cream/white tops or plain dark shirts with jeans. Sibling girls can wear cream/white shirts/tank tops with jeans or cream/white dresses.<br><b>I do not recommend bringing toddlers/children for the entire session. It is very hot in my studio and there is not adequate room for them to play, which makes them unhappy! Please plan to bring them for photos at the beginning of the session, and have dad or a grandparent take them out for an activity while we finish the session.</b></p>
  </div>
</section>

<section class="page page--p5">
  <div class="photo p5-photo" role="img" aria-label="Client photo: toddler with a naked cake on a wood slice, paper flowers and a floral hoop on a cream backdrop"></div>
</section>

<section class="page page--p6">
  <div class="content">
    <h2 class="script-title" style="margin-top:0">What I need to know before your session</h2>
    <ol class="need-list">
      <li><span class="num">1</span><p>Please e-mail me with the baby's birth date, birth weight, sex, and name. Remember, my newborn sessions take place between 5-11 days old, so it is critical to e-mail me when baby arrives to schedule your session.</p></li>
      <li><span class="num">2</span><p>If you have any favorite colors please feel free to let me know and I will be happy to work them into your session. Please also let me know if there are any colors you do not want used during your session. You can create an account on my website and select a set of favorites, I will look at those before your session.</p></li>
      <li><span class="num">3</span><p>If you have specific shots in mind for your session, or any props you have seen on my website that you would like me to use, you must let me know in advance. It takes a lot of preparation for a session, so please tell me beforehand if you have a specific request.</p></li>
      <li><span class="num">4</span><p>Please let me know if you have any siblings you would like to include in the session and their age(s).</p></li>
    </ol>
    <h2 class="faq-title">FAQ'S</h2>
    <span class="faq-q">When I will see my photos?</span>
    <p class="faq-a">Your gallery of images will be e-mailed to you within 3 weeks. You will receive a preview photo of your session within 2 days.</p>
    <span class="faq-q">Can I share my gallery?</span>
    <p class="faq-a">Yes, you can share your gallery with anyone you like. Just send them the gallery link and password.</p>
    <span class="faq-q">How can I download my photos?</span>
    <p class="faq-a">You can download all of your high-resolution images directly from your gallery.<br>Please keep in mind that these are very large files – each photo can be up to 10 megabytes.</p>
  </div>
  <div class="circles">
    <div class="c1" role="img" aria-label="Client photo: sleeping newborn with lace on lavender"></div>
    <div class="c2" role="img" aria-label="Client photo: baby sitting with a white teddy bear"></div>
    <div class="c3" role="img" aria-label="Client photo: sleeping newborn on blush fabric"></div>
  </div>
</section>

</body>
</html>
```